Honey Jar Label Design

I am looking for a fun label design for a 1 lb honey jar.
The company is Corliss Waverly Botanicals, which sells cut flowers and is expanding into honey and eventually other honey products. I've included the design work for the business, and I'd like the honey products to coordinate with them but not necessarily match directly.
Label requirements:
Raw Honey
Corliss Waverly Botanicals
27308 Quarry Bend Rd
Eudora, KS 66341
NET WT. 16 OZ. (weight info must be in the lower third of the front label and easy to read)
Look and feel
Each slider illustrates characteristics of the customer's brand and the style your logo design should communicate.

```html
<!DOCTYPE html>
<html lang="en">
<head>
<meta charset="utf-8">
<title>Raw Honey Label – Corliss Waverly Botanicals</title>
<link href="https://fonts.googleapis.com/css2?family=Kaushan+Script&family=Poppins:wght@400;600&display=swap" rel="stylesheet">
<style>
  :root {
    --honey-yellow: #ffc20e;
    --label-charcoal: #333234;
    --brand-teal: #123c3c;
    --paper-white: #ffffff;
    --text-light: #f4f1ea;
  }
  html, body {
    margin: 0;
    padding: 0;
    width: 1200px;
    height: 672px;
    overflow: hidden;
    background: var(--honey-yellow);
  }
  .canvas {
    position: relative;
    width: 1200px;
    height: 672px;
    background: var(--honey-yellow);
  }
  .label-shape {
    position: absolute;
    inset: 0;
  }
  .brand-name {
    font-family: "Poppins", sans-serif;
    font-weight: 600;
    fill: var(--brand-teal);
    letter-spacing: 1px;
  }
  .product-title {
    font-family: "Kaushan Script", cursive;
    fill: var(--honey-yellow);
  }
  .address {
    font-family: "Poppins", sans-serif;
    font-weight: 400;
    fill: var(--text-light);
  }
  .net-weight {
    font-family: "Poppins", sans-serif;
    font-weight: 600;
    fill: var(--honey-yellow);
  }
</style>
</head>
<body>
<main class="canvas">
  <svg class="label-shape" width="1200" height="672" viewBox="0 0 1200 672" xmlns="http://www.w3.org/2000/svg">
    <defs>
      <linearGradient id="bee-tones" x1="0" y1="0" x2="0" y2="1">
        <stop offset="0" stop-color="#6b4a1c"/>
        <stop offset="0.55" stop-color="#c98f1e"/>
        <stop offset="1" stop-color="#2a1d10"/>
      </linearGradient>
    </defs>

    <!-- label body -->
    <polygon class="label-body"
      points="600,48 841,186 841,488 600,624 359,488 359,186"
      fill="var(--label-charcoal)" stroke="var(--label-charcoal)"
      stroke-width="14" stroke-linejoin="round"/>

    <!-- inner keyline -->
    <polygon class="label-keyline"
      points="600,66 829,195 829,480 600,606 371,480 371,195"
      fill="none" stroke="var(--honey-yellow)" stroke-width="1"/>

    <!-- brand seal -->
    <circle class="brand-seal" cx="597" cy="222" r="103" fill="var(--paper-white)"/>
    <circle class="brand-seal-ring" cx="597" cy="222" r="98" fill="none" stroke="var(--honey-yellow)" stroke-width="1.5"/>
    <text class="brand-name" x="594" y="217" text-anchor="middle" font-size="14">CORLISS WAVERLY</text>
    <text class="brand-name" x="594" y="238" text-anchor="middle" font-size="14">BOTANICALS</text>

    <!-- bee illustration area -->
    <rect class="bee-illustration" role="img" aria-label="Illustration of a honey bee perched on the seal"
      x="688" y="172" width="70" height="166" rx="33" fill="url(#bee-tones)"/>

    <!-- product name -->
    <text class="product-title" x="600" y="422" text-anchor="middle" font-size="88">Raw Honey</text>

    <!-- address -->
    <text class="address" x="600" y="482" text-anchor="middle" font-size="21">27308 Quarry Bend Rd</text>
    <text class="address" x="600" y="508" text-anchor="middle" font-size="21">Eudora, KS 66341</text>

    <!-- weight -->
    <text class="net-weight" x="600" y="551" text-anchor="middle" font-size="21">NET WT. 16 OZ.</text>
  </svg>
</main>
</body>
</html>
```